A5 Flyer for Financial Services Business

I am after a re-design of our business flyer to fit in with our new branding style and logo colour scheme. Wanting something with a bit of designer flair that I could not create myself. I have included the flyer which I created which lacks style so dazzle me.

I want to use the same content.

Text for main body of flyer is

Are you a small business owner, tradie or PAVC Service Provider struggling to stay on top of your bookkeeping and compliance obligations? If so we would love to help you get back on track and take control of your business finances so that you can make informed business decisions and focus on what you do best.

We have over 20 years industry experience and, as a small business ourselves, we are able to offer our clients a personal bookkeeping solution tailored to meet the needs of your business.

Accounts Payable | Accounts Receivable
Customer Invoicing
Bank and Credit Card Reconciliations
Payroll | Superannuation | Payroll Tax
Business Activity | Instalment Activity Statements
Regular Financial Reports
Ledgerly and Tallybooks Set-Up and Training

```html
<!DOCTYPE html>
<html lang="en">
<head>
<meta charset="utf-8">
<title>Even Keel Financial Services – Bookkeeping Flyer</title>
<link href="https://fonts.googleapis.com/css2?family=Poppins:wght@300;500;600;700;800&family=Montserrat:wght@400;500;700&display=swap" rel="stylesheet">
<style>
  :root{
    --navy:#0b3a58;
    --navy-deep:#082e49;
    --teal:#0f8a8d;
    --teal-panel:#137b83;
    --teal-light:#1aa3a6;
    --grey-chevron:#9aa1a6;
    --badge-grey:#d9dee1;
    --ink:#1d1d1d;
    --white:#ffffff;
    --gold:#f2b632;
    --page:#d0d0d0;
  }
  *{box-sizing:border-box;margin:0;padding:0}
  html,body{width:864px;height:1200px;overflow:hidden;background:var(--page)}
  .flyer{position:absolute;left:9px;top:0;width:846px;height:1200px;background:var(--white);overflow:hidden;font-family:"Montserrat",sans-serif;color:var(--ink)}
  .flyer-art{position:absolute;left:0;top:0;width:846px;height:1200px}
  .brand{position:absolute;left:40px;top:40px;width:280px;text-align:center;color:var(--teal);font-family:"Poppins",sans-serif;font-weight:300}
  .brand-dot{width:58px;height:58px;border-radius:50%;background:var(--teal);margin:0 auto 12px}
  .brand-name{font-size:30px;line-height:32px;letter-spacing:.5px}
  .brand-sub{font-size:15px;letter-spacing:6px;margin-top:2px}
  .headline{position:absolute;left:45px;top:213px;font-family:"Poppins",sans-serif;font-weight:800;font-size:40px;line-height:42px;color:var(--white);text-transform:uppercase;letter-spacing:.3px}
  .intro{position:absolute;left:45px;top:370px;width:482px}
  .intro-question{font-family:"Poppins",sans-serif;font-weight:700;font-size:20.5px;line-height:24px;color:var(--navy)}
  .intro-body{font-size:15.4px;line-height:19.3px;margin-top:6px;color:var(--ink)}
  .intro-body + .intro-body{margin-top:7px}
  .intro-body strong{color:var(--navy);font-weight:700}
  .experience{position:absolute;left:562px;top:385px;width:248px;text-align:center;color:var(--white);font-family:"Poppins",sans-serif}
  .stars{color:var(--gold);font-size:24px;letter-spacing:3px;line-height:28px}
  .exp-over{font-size:22px;letter-spacing:3px;font-weight:500;margin-top:12px;line-height:30px}
  .exp-row{display:flex;align-items:center;justify-content:center;gap:4px;margin-top:2px}
  .exp-number{font-size:96px;font-weight:800;line-height:92px;letter-spacing:-8px;background:linear-gradient(90deg,var(--teal-light) 50%,var(--white) 50%);-webkit-background-clip:text;background-clip:text;-webkit-text-fill-color:transparent;padding-right:8px}
  .exp-words{text-align:left}
  .exp-years{font-size:38px;font-weight:700;line-height:38px}
  .exp-industry{font-size:18px;letter-spacing:3.5px;font-weight:500;line-height:22px}
  .exp-tag{display:inline-block;background:var(--teal-light);font-size:18px;font-weight:700;line-height:22px;padding:0 4px;margin-top:3px}
  .services{position:absolute;top:640px;list-style:none;font-family:"Poppins",sans-serif;font-weight:600;font-size:22px;line-height:26px;color:var(--white)}
  .services-left{left:48px}
  .services-right{left:454px}
  .service{position:absolute;left:0;display:flex;align-items:center;width:370px}
  .service-icon{flex:0 0 50px;width:50px;height:50px;margin-right:8px}
  .contact-tab{position:absolute;left:0;top:1021px;width:319px;height:35px;background:var(--navy);color:var(--white);font-family:"Poppins",sans-serif;font-weight:700;font-size:23px;line-height:35px;padding-left:52px;border-radius:0 6px 6px 0;box-shadow:0 3px 5px rgba(0,0,0,.3)}
  .contact-phone{position:absolute;left:45px;top:1064px;display:flex;align-items:center;gap:8px;font-family:"Poppins",sans-serif;font-weight:700;font-size:32px;line-height:40px;color:var(--ink)}
  .contact-line{position:absolute;left:45px;display:flex;align-items:center;gap:10px;font-weight:700;font-size:14.6px;color:var(--ink)}
  .contact-email{top:1106px}
  .contact-web{top:1130px}
  .contact-line svg,.contact-phone svg{flex:0 0 auto}
  .agent-note{position:absolute;left:509px;top:1122px;width:50px;text-align:center;font-size:6px;line-height:7px;color:var(--ink)}
</style>
</head>
<body>
<div class="flyer">
  <svg class="flyer-art" viewBox="0 0 846 1200">
    <defs>
      <linearGradient id="bandGrad" x1="0" y1="0" x2="1" y2="0">
        <stop offset="0" stop-color="#0a3556"/>
        <stop offset="0.55" stop-color="#0c5f74"/>
        <stop offset="1" stop-color="#11938f"/>
      </linearGradient>
      <linearGradient id="triGrad" x1="0" y1="0" x2="0" y2="1">
        <stop offset="0" stop-color="#0b5f6e"/>
        <stop offset="1" stop-color="#12a29b"/>
      </linearGradient>
      <linearGradient id="photoGrad" x1="0" y1="0" x2="1" y2="1">
        <stop offset="0" stop-color="#d9d3c9"/>
        <stop offset="0.5" stop-color="#eeeae4"/>
        <stop offset="1" stop-color="#8d9db1"/>
      </linearGradient>
      <linearGradient id="panelGrad" x1="0" y1="0" x2="1" y2="1">
        <stop offset="0" stop-color="#137a82"/>
        <stop offset="1" stop-color="#0f6f79"/>
      </linearGradient>
      <linearGradient id="badgeGrad" x1="0" y1="0" x2="0" y2="1">
        <stop offset="0" stop-color="#0a3a58"/>
        <stop offset="1" stop-color="#0b4a66"/>
      </linearGradient>
    </defs>
    <polygon points="520,0 846,0 846,356 538,356 438,125" fill="url(#photoGrad)" role="img" aria-label="Photo of hands working with a calculator, pen and financial charts on a desk"/>
    <polygon points="352,0 520,0 436,123" fill="url(#triGrad)"/>
    <polygon points="415,150 438,125 538,356 513,356" fill="var(--grey-chevron)"/>
    <polygon points="0,197 440,197 536,359 0,359" fill="url(#bandGrad)"/>
    <polygon points="552,616 552,369 683,304 820,369 820,616" fill="var(--teal)"/>
    <polygon points="562,616 562,377 683,316 810,377 810,616" fill="url(#badgeGrad)"/>
    <rect x="0" y="616" width="846" height="386" fill="url(#panelGrad)"/>
    <line x1="411" y1="643" x2="411" y2="980" stroke="rgba(255,255,255,.35)" stroke-width="1"/>
    <circle cx="534" cy="1087" r="28" fill="var(--badge-grey)" role="img" aria-label="Registered agent badge"/>
    <circle cx="638" cy="1095" r="30" fill="var(--badge-grey)" role="img" aria-label="Certified advisor badge"/>
    <rect x="721" y="1062" width="62" height="62" rx="4" fill="var(--badge-grey)" role="img" aria-label="Certified advisor badge"/>
  </svg>

  <div class="brand">
    <div class="brand-dot"></div>
    <div class="brand-name">EVEN KEEL</div>
    <div class="brand-sub">Financial Services</div>
  </div>

  <h1 class="headline">Bookkeeping<br>tailored to your<br>business needs</h1>

  <div class="intro">
    <p class="intro-question">Are you a small business owner, tradie or PAVC Service Provider struggling to stay on top of your bookkeeping and compliance obligations?</p>
    <p class="intro-body">If so we would love to help you get back on track and take control of your business finances so that you can make informed business decisions and focus on what you do best.</p>
    <p class="intro-body">As a small business ourselves, we are able to offer our clients a <strong>personal bookkeeping solution</strong> tailored to meet the needs of your business.</p>
  </div>

  <div class="experience">
    <div class="stars">★★★</div>
    <div class="exp-over">WE HAVE OVER</div>
    <div class="exp-row">
      <div class="exp-number">20</div>
      <div class="exp-words">
        <div class="exp-years">YEARS</div>
        <div class="exp-industry">INDUSTRY</div>
        <div class="exp-tag">EXPERIENCE</div>
      </div>
    </div>
  </div>

  <svg width="0" height="0" style="position:absolute">
    <defs>
      <symbol id="svc-icon" viewBox="0 0 50 50">
        <circle cx="25" cy="25" r="24" fill="none" stroke="#fff" stroke-width="1.2" stroke-dasharray="3 2"/>
        <circle cx="25" cy="25" r="20" fill="#fff"/>
        <rect x="17" y="14" width="16" height="21" rx="1.5" fill="none" stroke="#0b3a58" stroke-width="1.6"/>
        <line x1="20" y1="20" x2="30" y2="20" stroke="#0b3a58" stroke-width="1.4"/>
        <line x1="20" y1="24" x2="30" y2="24" stroke="#0b3a58" stroke-width="1.4"/>
        <line x1="20" y1="28" x2="26" y2="28" stroke="#0b3a58" stroke-width="1.4"/>
        <circle cx="31" cy="32" r="4.5" fill="#fff" stroke="#0f8a8d" stroke-width="1.6"/>
      </symbol>
    </defs>
  </svg>

  <ul class="services services-left">
    <li class="service" style="top:-6px"><svg class="service-icon"><use href="#svc-icon"/></svg>Accounts Payable</li>
    <li class="service" style="top:56px"><svg class="service-icon"><use href="#svc-icon"/></svg>Accounts Receivable</li>
    <li class="service" style="top:114px"><svg class="service-icon"><use href="#svc-icon"/></svg>Customer Invoicing</li>
    <li class="service" style="top:178px"><svg class="service-icon"><use href="#svc-icon"/></svg>Bank and Credit Card<br>Reconciliations</li>
    <li class="service" style="top:234px"><svg class="service-icon"><use href="#svc-icon"/></svg>Payroll</li>
    <li class="service" style="top:293px"><svg class="service-icon"><use href="#svc-icon"/></svg>Superannuation</li>
  </ul>
  <ul class="services services-right">
    <li class="service" style="top:-6px"><svg class="service-icon"><use href="#svc-icon"/></svg>Payroll Tax</li>
    <li class="service" style="top:60px"><svg class="service-icon"><use href="#svc-icon"/></svg>Business Activity<br>Statements</li>
    <li class="service" style="top:121px"><svg class="service-icon"><use href="#svc-icon"/></svg>Instalment Activity<br>Statements</li>
    <li class="service" style="top:190px"><svg class="service-icon"><use href="#svc-icon"/></svg>Ledgerly and Tallybooks<br>Set-Up and Training</li>
    <li class="service" style="top:252px"><svg class="service-icon"><use href="#svc-icon"/></svg>Regular Financial Reports</li>
  </ul>

  <div class="contact-tab">CONTACT US TODAY</div>
  <div class="contact-phone">
    <svg width="24" height="24" viewBox="0 0 24 24"><path d="M6.6 10.8a15 15 0 0 0 6.6 6.6l2.2-2.2a1 1 0 0 1 1-.25 11.4 11.4 0 0 0 3.6.57 1 1 0 0 1 1 1V20a1 1 0 0 1-1 1A17 17 0 0 1 3 4a1 1 0 0 1 1-1h3.5a1 1 0 0 1 1 1c0 1.25.2 2.45.57 3.6a1 1 0 0 1-.25 1z" fill="var(--navy)"/></svg>
    0412 555 019
  </div>
  <div class="contact-line contact-email">
    <svg width="22" height="14" viewBox="0 0 22 14"><rect x="1" y="1" width="20" height="12" fill="none" stroke="var(--navy)" stroke-width="2"/><path d="M1 1 l10 7 l10 -7" fill="none" stroke="var(--navy)" stroke-width="2"/></svg>
    info@evenkeelfinancialservices.com.au
  </div>
  <div class="contact-line contact-web">
    <svg width="22" height="22" viewBox="0 0 22 22"><circle cx="11" cy="11" r="9" fill="none" stroke="var(--navy)" stroke-width="2"/><ellipse cx="11" cy="11" rx="4" ry="9" fill="none" stroke="var(--navy)" stroke-width="1.5"/><line x1="2" y1="11" x2="20" y2="11" stroke="var(--navy)" stroke-width="1.5"/></svg>
    www.evenkeelfinancialservices.com.au
  </div>
  <div class="agent-note">BAS agent<br>10482273</div>
</div>
</body>
</html>
```